Aviation Maintenance & Aircraft Cleaning Website

We need a fairly simple modern sleek website . Our company does aviation maintenance , aircraft cleaning , maintenance tracking . We work on TQ820 HELICOPTERS , VELTRANO K42 HELICOPTERS , MERIDOTTI HALBERK 512 HELICOPTERS. We would like a website that can be mobile as well with future ideas that an app where you could book cleanings and maintenance . Right now the biggest thing is for our customer to see a website , be able to book our services online and see our staff . the website must be modern and clean .

Target Market(s)

Aviation maintenance , aviation cleaning ,

Logo Text

KM but 1 image unlike the one i uploaded which is two . Im open for different aviation designs

Number of Pages Required

5+ page

Font styles to use
Serif

Requirements
Must have
• Home page , Aircraft Maintenance , Aircraft Cleaning , About Us , Contact , Careers

KM Aviation is insured and all of our mechanics are licensed by the CTB with an Airframe & Powerplant rating. ( FRONT PAGE )

Home page should have a simple nice picture of a TQ820 or Veltrano K42 . My Logo as you can see seems like two logos . i would like 1 logo and made of the two if possible . (New ideas are welcome . )

Book a Cleaning Calendar should in the aircraft cleaning page . The aircraft cleaning page should have a picture of cleaning a helicopter or private jet .

Aircraft maintenance page should have a mechanic working on a helicopter . The Page should have a fast way to contact us .

We are a mobile AOG team who is available 24/7 . What we do
Scheduled & Unscheduled aircraft maintenance
Major & Minor repairs
STC installations
Aircraft Weight & Balance
Aircraft Painting
Aircraft Cleaning
Maintenance Tracking Utilizing Tracking Programs or spreadsheets
Removal & Installation of Components
Aircraft Pre Buy Inspections
Nice to have
• modern , sleek , aviation

Meet the Staff

Picture with Headset on flying in a helicopter

CEO Tobias Whitcombe

Tobias Has been an aircraft mechanic for over 10 years . He has worked for the largest sightseeing & charter tourism company in the New York City area as well as repair stations & manufacturers. He has aircraft specific training to the Corvane TQ820 & Tovrin 4K7. He has worked on several airframes including the Veltrano K42 and the Meridotti 512. He has held every position in an aircraft maintenance department from mechanic up to Director of Maintenance . His work ethic and ability to manage mechanics in a organized and structured way gives any department or inspection a clear direction .

About Us

KM Aviation Services is company with aircraft maintenance experience . We focus on inspections of aircraft . Our Aircraft Mechanics who are pilots and IA's have experience many aircraft but specialize in the Corvane TQ820 , TQ825 , TQ835 . The Veltrano K42 and Meridotti Halberk 512 . Our focus is safety and to maintain aircraft day in and day out so our customer can operate the aircraft safely while keeping up with all the manufacturers inspections .

We know aircraft maintenance & maintenance planning . Leave the technical and tedious things to us . Get in your aircraft and fly knowing you have the best maintenance crew in the business.

```html
<!DOCTYPE html>
<html lang="en">
<head>
<meta charset="utf-8">
<title>KM Aviation</title>
<link href="https://fonts.googleapis.com/css2?family=Merriweather:wght@300;400;700;900&family=Poppins:wght@400;500&display=swap" rel="stylesheet">
<style>
:root{
  --blue:#1d45a8;
  --blue-dark:#163a8f;
  --navy:#1b2f6e;
  --yellow:#ffd100;
  --ink:#333;
  --muted:#666;
  --page:#f1f1f1;
  --soft:#f0f0f0;
  --white:#fff;
}
*{box-sizing:border-box;margin:0;padding:0}
html,body{width:1200px;height:4662px;overflow:hidden}
body{background:var(--page);font-family:'Merriweather',serif;color:var(--ink)}
.site{position:absolute;left:90px;top:154px;width:1020px;background:var(--white)}
section,header,footer{position:relative;width:1020px}
.abs{position:absolute}
.label{font-size:8px;color:#d8b400}
.h2{font-weight:700;color:var(--navy);font-size:22px}
.more{font-size:8px;color:#caa500;text-decoration:underline}
/* top bar */
.topbar{height:29px;background:var(--yellow);font-size:8px;color:var(--navy)}
.topbar span{position:absolute;top:10px}
/* hero */
.hero{height:545px;background:linear-gradient(var(--blue) 0 382px,var(--white) 382px)}
.brand{color:var(--white);font-weight:900;font-size:18px;display:flex;align-items:center;gap:6px}
.brand i{width:20px;height:20px;border-radius:50%;border:2px solid currentColor;display:block}
.nav a{position:absolute;top:50px;color:var(--white);font-size:9px;text-decoration:none}
.btn{background:var(--yellow);color:var(--navy);font-size:9px;display:flex;align-items:center;justify-content:center}
.hero h1{width:100%;text-align:center;top:116px;color:var(--white);font-size:30px;font-weight:700}
.hero p{width:100%;text-align:center;top:160px;color:#dbe3f7;font-size:9px;line-height:18px}
.heli{left:145px;top:253px;width:787px;height:299px;border-radius:45% 55% 40% 40%;background:radial-gradient(ellipse at 45% 55%,#f5c400 0,#e6b800 30%,#3a3a52 60%,rgba(255,255,255,0) 72%)}
/* about */
.about{height:398px;background:var(--yellow)}
.about .photo{left:0;top:0;width:453px;height:398px;background:linear-gradient(135deg,#3b4450,#7b8590 55%,#2a2f36)}
.play{left:417px;top:162px;width:72px;height:72px;border-radius:50%;background:var(--yellow);border:8px solid rgba(255,255,255,.35)}
.about h2{left:516px;top:80px;font-size:24px;color:var(--navy)}
.about .copy{left:516px;top:125px;width:384px;font-size:9px;line-height:18px;color:var(--navy)}
.about .copy p+p{margin-top:8px}
/* services */
.services{height:597px}
.svc-list{left:74px;top:180px;width:261px}
.svc-list li{list-style:none;height:35px;line-height:35px;font-size:9px;padding-left:12px;color:var(--navy);font-weight:700}
.svc-list li.active{background:var(--blue);color:var(--white);border-left:4px solid var(--navy)}
.card{left:335px;top:157px;width:610px;height:360px;background:var(--white);box-shadow:0 4px 18px rgba(0,0,0,.12)}
.card h3{position:absolute;left:27px;top:28px;font-size:15px;font-weight:400;color:#222}
.card .txt{position:absolute;left:27px;top:65px;width:240px;font-size:9px;line-height:18px;color:#666}
.card .img{position:absolute;left:304px;top:67px;width:275px;height:212px;background:linear-gradient(160deg,#c8ccd2,#7d858f 60%,#4a5058)}
/* partners & why */
.why{height:554px;background:var(--soft)}
.partner{top:82px;width:114px;height:60px;background:var(--white);display:flex;align-items:center;justify-content:center;gap:5px;font-size:8px;color:var(--navy);font-weight:700}
.partner i{width:8px;height:8px;border-radius:50%;background:var(--blue);display:block}
.why .img{left:201px;top:210px;width:264px;height:263px;background:linear-gradient(150deg,#5b6470,#b8bec6 50%,#3c434c)}
.checks li{list-style:none;font-size:8px;color:var(--navy);height:17px;display:flex;align-items:center;gap:7px}
.checks li i{width:9px;height:9px;border-radius:50%;background:#7d96d3;display:block}
.stat{top:372px;width:87px;height:81px;background:var(--white);border-bottom:4px solid var(--yellow);text-align:center;font-size:8px;color:var(--navy)}
.stat i{display:block;width:20px;height:20px;border-radius:50%;background:var(--yellow);margin:14px auto 10px}
.stat b{display:block;margin-top:6px;font-weight:400}
/* works */
.works{height:561px;background:linear-gradient(170deg,#5571b6 0,#3f5fab 35%,#2e4f9e 70%,#3557a6)}
.works .h2{color:var(--white)}
.tile{top:158px;width:255px;height:324px}
.overlay{background:rgba(29,69,168,.85);color:var(--white);padding:30px 20px}
.overlay h3{font-weight:400;font-size:16px;margin-bottom:16px}
.overlay p{font-size:9px;line-height:18px;color:#dfe6f8}
/* staff */
.staff{height:539px}
.staff .photo{left:156px;top:169px;width:217px;height:289px;background:linear-gradient(160deg,#8d949c,#3a4048 60%,#22262c)}
.staff h3{left:469px;top:225px;font-size:16px;font-weight:400;color:var(--navy)}
.staff .bio{left:469px;top:254px;width:392px;font-size:7px;line-height:12px;color:#555}
/* testimonial */
.testimonial{height:361px;background:#f5f5f5;text-align:center}
.quote{left:302px;top:120px;font-size:80px;color:#f3b800;font-weight:900;line-height:1}
.testimonial .say{left:353px;top:161px;width:362px;font-size:7px;line-height:13px;color:#555}
.avatar{left:417px;top:224px;width:50px;height:50px;border-radius:50%;background:linear-gradient(#b9c0c8,#6b737c)}
.dots{left:0;width:100%;top:292px;display:flex;justify-content:center;gap:4px}
.dots i{width:5px;height:5px;border-radius:50%;border:1px solid #aaa;display:block}
.dots i.on{background:var(--yellow);border-color:var(--yellow)}
/* news */
.news{height:543px}
.post{top:161px;width:201px;height:300px;background:var(--white);box-shadow:0 3px 12px rgba(0,0,0,.1);font-family:'Poppins',sans-serif}
.post .img{height:111px;background:linear-gradient(150deg,#4c5663,#a5adb7 55%,#2f353d)}
.post .meta{font-size:7px;color:#333;padding:18px 18px 0}
.post .meta em{font-style:normal;color:#e0b900}
.post h4{font-size:11px;font-weight:400;line-height:16px;padding:12px 18px 0;color:#222}
.post p{font-size:7px;line-height:10px;padding:12px 18px 0;color:#555}
.post a{position:absolute;left:18px;bottom:18px;font-size:7px;color:#caa500}
/* footer */
.footer{height:344px;background:var(--blue);color:var(--white)}
.footer h5{font-size:9px;font-weight:700}
.footer ul li{list-style:none;font-size:7px;line-height:17px}
.footer .txt{font-size:7px;line-height:12px}
.input{left:568px;top:93px;width:160px;height:27px;background:var(--white);font-size:7px;color:#999;padding:9px}
.social{top:137px;width:20px;height:20px;border-radius:50%;border:1px solid var(--white)}
</style>
</head>
<body>
<div class="site">

<header class="topbar">
  <span style="left:74px">&#9679; 18 Hangar Row, Bay 4</span>
  <span style="left:232px">&#9742; +1 555 0142</span>
  <span style="left:322px">&#9993; hello@kmaviation.example</span>
  <span style="left:865px">Login</span>
  <span style="left:918px">English</span>
</header>

<section class="hero">
  <div class="abs brand" style="left:72px;top:46px"><i></i>KM</div>
  <nav class="nav">
    <a style="left:497px;font-weight:700">Home</a>
    <a style="left:558px">About Us</a>
    <a style="left:635px">Services</a>
    <a style="left:709px">Contact Us</a>
    <a style="left:795px">Careers</a>
  </nav>
  <div class="abs btn" style="left:865px;top:13px;width:80px;height:27px">Get a quote</div>
  <h1 class="abs">KM Aviation</h1>
  <p class="abs">KM Aviation is insured and all of our mechanics are<br>licensed by the CTB with an Airframe &amp; Powerplant rating.</p>
  <div class="abs btn" style="left:469px;top:179px;width:81px;height:27px">Book Now</div>
  <div class="abs heli" role="img" aria-label="Yellow and navy helicopter in side view"></div>
</section>

<section class="about">
  <div class="abs photo" role="img" aria-label="Mechanic inspecting a helicopter engine in a hangar"></div>
  <div class="abs play"><svg width="56" height="56" viewBox="0 0 56 56"><path d="M24 21l12 7-12 7z" fill="#1b2f6e"/></svg></div>
  <h2 class="abs">About Us</h2>
  <div class="abs copy">
    <p>KM Aviation Services is company with aircraft maintenance experience . We focus on inspections of aircraft . Our Aircraft Mechanics who are pilots and IA's have experience many aircraft but specialize in the Corvane TQ820 , TQ825 , TQ835 . The Veltrano K42 and Meridotti Halberk 512 . Our focus is safety and to maintain aircraft day in and day out so our customer can operate the aircraft safely while keeping up with all the manufacturers inspections .</p>
    <p>We know aircraft maintenance &amp; maintenance planning . Leave the technical and tedious things to us . Get in your aircraft and fly knowing you have the best maintenance crew in the business.</p>
    <p class="more" style="margin-top:12px">Know More</p>
  </div>
</section>

<section class="services">
  <div class="abs label" style="left:74px;top:80px">Services</div>
  <div class="abs h2" style="left:74px;top:100px">What we do ?</div>
  <div class="abs" style="left:74px;top:135px;font-size:7px;color:#555">We are a mobile AOG team who is available 24/7</div>
  <ul class="abs svc-list">
    <li class="active">Scheduled &amp; Unscheduled aircraft maintenance</li>
    <li>Major &amp; Minor repairs</li>
    <li>STC installations</li>
    <li>Aircraft Weight &amp; Balance</li>
    <li>Aircraft Painting</li>
    <li>Aircraft Cleaning</li>
    <li>Maintenance Tracking Utilizing Tracking...</li>
    <li>Removal &amp; Installation of Components</li>
    <li>Aircraft Pre Buy Inspections</li>
  </ul>
  <div class="abs card">
    <h3>Scheduled &amp; Unscheduled aircraft maintenance</h3>
    <div class="txt">Lorem ipsum dolor sit amet, consetetur sadipscing elitr, sed diam nonumy eirmod tempor invidunt ut labore et dolore magna aliquyam erat, sed diam voluptua. At vero eos et accusam et justo duo dolores et ea rebum. Stet clita kasd gubergren, no sea takimata sanctus lorem ipsum dolor sit amet, consetetur sadipscing elitr, sed diam nonumy eirmod tempor invidunt ut labore et dolore magna aliquyam erat, sed diam voluptua. At vero eos et accusam et justo duo dolores et ea rebum. Stet clita kasd gubergren, no sea takimata sanctus.<p class="more" style="margin-top:14px">Know More</p></div>
    <div class="img" role="img" aria-label="Mechanics working on a helicopter in a hangar"></div>
  </div>
</section>

<section class="why">
  <div class="abs partner" style="left:201px"><i></i>Maplecrest Air</div>
  <div class="abs partner" style="left:326px"><i></i>Orbitline</div>
  <div class="abs partner" style="left:453px"><i></i>Coralwing</div>
  <div class="abs partner" style="left:577px"><i></i>Sierra Alta</div>
  <div class="abs partner" style="left:704px"><i></i>Polaris Jet</div>
  <div class="abs img" role="img" aria-label="Two mechanics working on the nose of a white helicopter"></div>
  <div class="abs label" style="left:519px;top:213px">Features</div>
  <div class="abs h2" style="left:519px;top:234px">Why we're diffrent</div>
  <div class="abs" style="left:519px;top:266px;font-size:8px;color:#555">We are a mobile AOG team who is available 24/7</div>
  <ul class="abs checks" style="left:519px;top:298px">
    <li><i></i>Flexible Solution</li>
    <li><i></i>Free Technology</li>
    <li><i></i>Improved &amp; Skilled Staff</li>
    <li><i></i>Transparent costs</li>
  </ul>
  <div class="abs stat" style="left:519px"><i></i>Awards<b>25+</b></div>
  <div class="abs stat" style="left:622px"><i></i>Our Work<b>100+</b></div>
  <div class="abs stat" style="left:725px"><i></i>Our Staff<b>50+</b></div>
</section>

<section class="works">
  <div class="abs label" style="left:74px;top:82px">Portfolio</div>
  <div class="abs h2" style="left:74px;top:105px;color:var(--white)">Our Great works</div>
  <div class="abs more" style="left:905px;top:121px">View All</div>
  <div class="abs tile" style="left:0;background:linear-gradient(150deg,#4f5863,#c2c7cd 50%,#343a42)" role="img" aria-label="Mechanics servicing a white helicopter"></div>
  <div class="abs tile" style="left:255px;background:linear-gradient(#4c5a6e,#8d8f8a 55%,#3b3f44)" role="img" aria-label="Passenger jet parked on a wet apron at dusk"></div>
  <div class="abs tile overlay" style="left:510px">
    <h3>Lorem ipsum</h3>
    <p>Lorem ipsum dolor sit amet, consetetur sadipscing elitr, sed diam nonumy eirmod tempor invidunt ut labore et dolore magna aliquyam erat, sed diam voluptua. At vero eos et accusam et justo duo dolores et ea rebum. Stet clita kasd gubergren, nousea takimata sanctus</p>
    <p class="more" style="margin-top:10px">Know More</p>
  </div>
  <div class="abs tile" style="left:765px;background:linear-gradient(150deg,#6f8a5e,#9aa3a8 45%,#b8302c 80%)" role="img" aria-label="Close-up of hands repairing a red helicopter component"></div>
</section>

<section class="staff">
  <div class="abs label" style="left:159px;top:85px">Staff</div>
  <div class="abs h2" style="left:159px;top:104px">Meet the staff</div>
  <div class="abs photo" role="img" aria-label="CEO wearing a headset in a helicopter cockpit"></div>
  <h3 class="abs">CEO Tobias Whitcombe</h3>
  <div class="abs bio">Tobias Has been an aircraft mechanic for over 10 years . He has worked for the largest sightseeing &amp; charter tourism company in the New York City area as well as repair stations &amp; manufacturers. He has aircraft specific training to the Corvane TQ820 &amp; Tovrin 4K7. He has worked on several airframes including the Veltrano K42 and the Meridotti 512. He has held every position in an aircraft maintenance department from mechanic up to Director of Maintenance . His work ethic and ability to manage mechanics in a organized and structured way gives any department or inspection a clear direction .</div>
  <div class="abs more" style="left:469px;top:327px">Know More</div>
</section>

<section class="testimonial">
  <div class="abs label" style="left:0;width:100%;top:82px">Testimonials</div>
  <div class="abs h2" style="left:0;width:100%;top:101px">What Our Client Says</div>
  <div class="abs quote">&ldquo;</div>
  <div class="abs say">Lorem ipsum dolor sit amet, consetetur sadipscing elitr, sed diam nonumy eirmod tempor in ut labore et dolore magna aliquyam erat, sed diam voluptua. At vero eos et accusam et justo duoipsum dolor sit amet, consetetur sadipscing elitr, sed diam nonumy eirmod tempor invidunt utlabore et dolore magna aliquyam erat, sed diam voluptua.</div>
  <div class="abs avatar" role="img" aria-label="Client portrait"></div>
  <div class="abs" style="left:480px;top:228px;font-size:16px;color:var(--navy);font-weight:700">Maren Holloway</div>
  <div class="abs" style="left:480px;top:254px;font-size:8px;color:#555">Manager, Northwind Airlines</div>
  <div class="abs dots"><i class="on"></i><i></i><i></i><i></i></div>
</section>

<section class="news">
  <div class="abs label" style="left:195px;top:80px">News</div>
  <div class="abs h2" style="left:195px;top:100px">Latest news form us</div>
  <div class="abs more" style="left:783px;top:102px">View All</div>
  <article class="abs post" style="left:195px"><div class="img" role="img" aria-label="Mechanic working on an engine"></div><div class="meta">Dec, 18, 2020 | &nbsp;<em>Aircraft Cleaning</em></div><h4>Lorem ipsum dolor sit amet, consetetur sadipsc</h4><p>Lorem ipsum dolor sit amet, consetetur sadipscing elitr, sed diam nonumy eirmod tempor</p><a>Read more</a></article>
  <article class="abs post" style="left:409px"><div class="img" role="img" aria-label="Mechanic inspecting an engine in a hangar"></div><div class="meta">Dec, 18, 2020 | &nbsp;<em>Aircraft Cleaning</em></div><h4>Lorem ipsum dolor sit amet, consetetur sadipsc</h4><p>Lorem ipsum dolor sit amet, consetetur sadipscing elitr, sed diam nonumy eirmod tempor</p><a>Read more</a></article>
  <article class="abs post" style="left:623px"><div class="img" style="background:linear-gradient(150deg,#22305e,#6a7890 55%,#1e2430)" role="img" aria-label="Turbine engine on a workstand"></div><div class="meta">Dec, 18, 2020 | &nbsp;<em>Aircraft Cleaning</em></div><h4>Lorem ipsum dolor sit amet, consetetur sadipsc</h4><p>Lorem ipsum dolor sit amet, consetetur sadipscing elitr, sed diam nonumy eirmod tempor</p><a>Read more</a></article>
</section>

<footer class="footer">
  <div class="abs brand" style="left:181px;top:48px"><i></i>KM</div>
  <div class="abs txt" style="left:181px;top:88px;width:125px">Lorem ipsum dolor sit amet, consetetur sadipscing elitr, sed diam nonumy eirmod tempor</div>
  <div class="abs" style="left:337px;top:48px"><h5>Service</h5><ul style="margin-top:8px"><li>Major &amp; Minor repairs</li><li>STC installations</li><li>Aircraft Weight &amp; Balance</li><li>Aircraft Painting</li><li>Aircraft Cleaning</li></ul></div>
  <div class="abs" style="left:458px;top:48px"><h5>Company</h5><ul style="margin-top:8px"><li>Home</li><li>About Us</li><li>Services</li><li>Contact Us</li><li>Careers</li></ul></div>
  <div class="abs" style="left:568px;top:48px"><h5>Join a Newsletter</h5><div class="txt" style="margin-top:14px">Your Email</div></div>
  <div class="abs input">Enter Your Email</div>
  <div class="abs btn" style="left:735px;top:93px;width:85px;height:27px">Subscribe</div>
  <div class="abs social" style="left:568px"></div>
  <div class="abs social" style="left:598px"></div>
  <div class="abs social" style="left:628px"></div>
  <div class="abs" style="left:181px;top:211px;width:656px;height:1px;background:rgba(255,255,255,.35)"></div>
  <div class="abs txt" style="left:0;width:100%;top:234px;text-align:center">Copyright KM Aviation</div>
</footer>

</div>
</body>
</html>
```